Web Design for Real Estate Lending business

I need a web design for my real estate private lending business. The name of the business is Halvane Capital Group. I plan on using Wordpress because that platform is the most optimized for SEO, and we will rely heavily on SEO after the website is built.

I want the website to be responsive of course, and have a fresh, professional, and sleek UI.

The 4 main goals of the website will be:
1. Rank in Zonplex for our relevant key words (Los Angeles real estate hard money lending, real estate financing, fix and flip, private lending, etc)
2. Educate them on what our lending platform is capable of.
3. Capture the contact info (email or phone number) of investors & borrowers who are interested
4. Encourage investors and borrowers to contact us directly

This is an example of a similar business's website: https://www.dorvelcapital.example/

Here is my business parter's old website:
https://web.pastvault.example/web/20180822043430/http://www.melrocg.example/

All of the information on that website (2nd link) will apply to our business. You can pull the information from that Melro CG website and make it look more modern / sleek, similar to the 1st link (but better).

We are not selling anything on the website.

I also attached a business card template. I would like something similar to this but one that looks slightly more corporate / professional. Keep the colors the same though.

```html
<!DOCTYPE html>
<html lang="en">
<head>
<meta charset="utf-8">
<title>Halvane Capital Group</title>
<link href="https://fonts.googleapis.com/css2?family=Montserrat:wght@500;600;700;800&family=Open+Sans:wght@400;600;700&display=swap" rel="stylesheet">
<style>
:root{
  --blue:#1f5fc8;
  --blue-dark:#164a9e;
  --blue-light:#3a7be0;
  --ink:#1b1b1f;
  --text:#6b6f78;
  --line:#e2e5ea;
  --field:#eef0f3;
  --footer:#0d0f14;
  --white:#ffffff;
  --star:#e23b3b;
}
*{box-sizing:border-box;margin:0;padding:0}
html,body{width:1200px;height:3632px;overflow:hidden}
body{font-family:"Open Sans",Arial,sans-serif;color:var(--ink);background:var(--white);position:relative}
h1,h2,h3,h4,.btn,.brand{font-family:"Montserrat",Arial,sans-serif}
.lorem{font-size:14px;line-height:1.75;color:var(--text)}
.btn{display:inline-flex;align-items:center;height:44px;font-size:13px;font-weight:700;letter-spacing:.5px;color:var(--white);text-transform:uppercase}
.btn .label{background:var(--blue);height:100%;display:flex;align-items:center;padding:0 24px}
.btn .arrow{background:var(--blue-dark);width:44px;height:100%;display:flex;align-items:center;justify-content:center;margin-left:4px}
.btn.ghost .label,.btn.ghost .arrow{background:transparent;border:1.5px solid rgba(255,255,255,.8)}
.circle{width:22px;height:22px;border-radius:50%;background:var(--blue);display:inline-block}

/* top bar */
.topbar{position:absolute;top:0;left:0;width:1200px;height:40px;display:flex;align-items:center;justify-content:space-between;padding:0 110px;font-size:13px}
.topbar .socials{display:flex;gap:10px}
.topbar .socials span{width:16px;height:16px;border-radius:50%;background:var(--blue)}
.topbar .contact{display:flex;gap:22px;align-items:center}
.topbar .contact div{display:flex;align-items:center;gap:8px}
/* nav */
.nav{position:absolute;top:40px;left:0;width:1200px;height:80px;display:flex;align-items:center;padding:0 110px;border-top:1px solid var(--line)}
.brand{display:flex;align-items:center;gap:12px;font-weight:800;font-size:20px;color:var(--blue-dark);line-height:1}
.brand .mark{width:34px;height:34px;background:var(--blue)}
.nav ul{list-style:none;display:flex;gap:30px;margin-left:auto;margin-right:34px;font-family:"Montserrat",sans-serif;font-size:13px;font-weight:600;text-transform:uppercase}
.nav .login{height:38px;padding:0 22px;background:var(--blue);color:#fff;font-family:"Montserrat",sans-serif;font-weight:700;font-size:13px;display:flex;align-items:center;gap:10px}
/* hero */
.hero{position:absolute;top:120px;left:0;width:1200px;height:580px;background:linear-gradient(180deg,#8ab3dc 0%,#4f7fae 45%,#36603d 78%,#2d4d2a 100%)}
.hero .content{position:absolute;left:110px;top:170px;color:#fff;width:330px}
.hero h1{font-size:54px;font-weight:800;line-height:1;text-transform:uppercase}
.hero p{font-size:14px;line-height:1.6;margin:14px 0 22px;color:rgba(255,255,255,.9)}
.hero .rail{position:absolute;right:30px;top:150px;display:flex;flex-direction:column;align-items:center;gap:12px}
.hero .rail span{width:14px;height:14px;border-radius:50%;background:rgba(255,255,255,.85)}
.hero .rail i{width:1px;height:60px;background:rgba(255,255,255,.6)}
.hero .rail em{font-style:normal;font-size:11px;color:#fff;writing-mode:vertical-rl}
/* about */
.about{position:absolute;top:800px;left:0;width:1200px;height:420px}
.about .photo-wrap{position:absolute;left:120px;top:20px;width:440px;height:370px}
.about .photo-wrap:before{content:"";position:absolute;left:-12px;top:-12px;width:150px;height:150px;background:var(--blue)}
.about .photo-wrap:after{content:"";position:absolute;right:-12px;bottom:-12px;width:150px;height:150px;background:var(--blue)}
.about .photo{position:absolute;inset:0;z-index:1;background:linear-gradient(135deg,#d8d4cf,#7a6a5e 55%,#3e3a3a)}
.about .text{position:absolute;left:630px;top:10px;width:450px}
h2.section{font-size:36px;font-weight:800;text-transform:uppercase}
.about h2{padding-left:20px;border-left:5px solid var(--blue);line-height:1}
.about .lorem{margin:22px 0 28px}
/* invest / borrow */
.split{position:absolute;top:1280px;left:0;width:1200px;height:400px;display:flex}
.split .half{flex:1;color:#fff;text-align:center;padding:120px 80px 0}
.split .invest{background:linear-gradient(135deg,#1d58bd,#1a4fa8)}
.split .borrow{background:linear-gradient(135deg,#3f84e6,#2f6fd2)}
.split h3{font-size:34px;font-weight:800;text-transform:uppercase}
.split p{font-size:13px;line-height:1.7;margin:18px 0 26px;color:rgba(255,255,255,.88)}
/* featured */
.featured{position:absolute;top:1745px;left:0;width:1200px}
.featured h2{text-align:center}
.cards{position:absolute;top:95px;left:120px;display:flex;gap:30px}
.card{width:300px;height:380px;border:1px solid var(--line);box-shadow:0 4px 14px rgba(0,0,0,.06)}
.card .img{height:170px}
.card .body{padding:22px 20px}
.card h4{font-size:13px;font-weight:700;text-transform:uppercase;margin-bottom:10px}
.card .lorem{font-size:13px;line-height:1.65}
.card .more{font-family:"Montserrat",sans-serif;font-size:13px;font-weight:700;color:var(--blue);margin-top:12px;display:flex;align-items:center;gap:6px}
/* testimonials */
.testimonials{position:absolute;top:2310px;left:0;width:1200px;height:450px;background:linear-gradient(135deg,#1e5cc4,#2c6bd6)}
.testimonials h2{color:#fff;text-align:center;margin-top:62px}
.quotes{position:absolute;top:150px;left:140px;display:flex;gap:40px}
.quote{width:440px;height:240px;background:#fff;padding:26px 28px;position:relative}
.quote .who{display:flex;align-items:center;gap:14px;margin-bottom:20px}
.quote .avatar{width:48px;height:48px;border-radius:50%;background:#b7a89a}
.quote h4{font-size:14px;font-weight:700;text-transform:uppercase}
.quote .stars{display:flex;gap:3px;margin-top:4px}
.quote .mark{position:absolute;right:28px;top:20px;font-family:"Montserrat",sans-serif;font-size:72px;font-weight:800;color:#e3e6eb;line-height:1}
/* contact */
.contact-form{position:absolute;top:2835px;left:0;width:1200px}
.contact-form h2{text-align:center}
.form{position:absolute;top:82px;left:220px;width:760px;display:grid;grid-template-columns:1fr 1fr;gap:14px 20px}
.field{height:40px;background:var(--field);border:1px solid var(--line);font-size:12px;padding:12px 14px;color:#444}
.field.wide{grid-column:1/3;height:80px}
.form .submit{grid-column:1/3;justify-self:center;margin-top:18px}
/* footer */
.footer{position:absolute;top:3280px;left:0;width:1200px;height:352px;background:var(--footer);color:#d5d8de}
.footer .cols{position:absolute;top:50px;left:110px;display:flex;gap:0}
.footer .col{width:235px}
.footer .col:first-child{width:220px}
.footer h4{font-family:"Montserrat",sans-serif;font-size:16px;font-weight:800;color:#fff;text-transform:uppercase;padding-bottom:8px;border-bottom:2px solid var(--blue);display:inline-block;margin-bottom:16px}
.footer .brand{color:#fff}
.footer p,.footer li{font-size:13px;line-height:1.7}
.footer ul{list-style:none}
.footer li{display:flex;align-items:center;gap:10px;margin-bottom:6px}
.footer li:before{content:"";width:0;height:0;border-left:6px solid var(--blue);border-top:4px solid transparent;border-bottom:4px solid transparent}
.footer .contact-list li:before{display:none}
.footer .follow{font-family:"Montserrat",sans-serif;font-weight:700;color:#fff;margin:16px 0 10px;font-size:14px}
.footer .follow-row{display:flex;gap:8px}
.footer .follow-row span{width:26px;height:26px;border-radius:50%;background:var(--blue)}
.footer .copy{position:absolute;bottom:0;left:0;width:1200px;height:44px;border-top:1px solid #2a2d34;display:flex;align-items:center;justify-content:center;font-size:12px;color:#9aa0aa}
</style>
</head>
<body>

<header class="topbar">
  <div class="socials"><span></span><span></span><span></span><span></span></div>
  <div class="contact">
    <div><span class="circle" style="width:18px;height:18px;display:flex;align-items:center;justify-content:center"><svg width="10" height="10" viewBox="0 0 24 24"><path fill="#fff" d="M6.6 10.8a15 15 0 0 0 6.6 6.6l2.2-2.2a1 1 0 0 1 1-.25 11 11 0 0 0 3.6.6 1 1 0 0 1 1 1V20a1 1 0 0 1-1 1A17 17 0 0 1 3 4a1 1 0 0 1 1-1h3.5a1 1 0 0 1 1 1c0 1.25.2 2.45.6 3.6a1 1 0 0 1-.25 1z"/></svg></span>555-0142-770</div>
    <div><span class="circle" style="width:18px;height:18px;display:flex;align-items:center;justify-content:center"><svg width="10" height="10" viewBox="0 0 24 24"><path fill="#fff" d="M2 5h20v14H2zm2 2v.5l8 5 8-5V7z"/></svg></span>info@halvanecapital.example</div>
  </div>
</header>

<nav class="nav">
  <div class="brand"><span class="mark"></span><span>HALVANE<br><span style="font-size:13px;font-weight:600">Capital Group</span></span></div>
  <ul><li>Home</li><li>About Us</li><li>Investors</li><li>Borrowers</li><li>Contact Us</li></ul>
  <div class="login"><svg width="12" height="12" viewBox="0 0 24 24"><path fill="#fff" d="M12 12a5 5 0 1 0 0-10 5 5 0 0 0 0 10zm0 2c-5 0-9 2.5-9 6v2h18v-2c0-3.5-4-6-9-6z"/></svg>Login</div>
</nav>

<section class="hero" role="img" aria-label="Photograph of a modern two-storey house with a lawn under a blue sky">
  <div class="content">
    <h1>Halvane Capital Group</h1>
    <p>Lorem ipsum dolor sit amet, consectetur adipiscing elit, sed do eiusmod tempor incididunt ut labore.</p>
    <div class="btn"><span class="label">Get Started</span><span class="arrow">→</span></div>
  </div>
  <div class="rail"><span></span><span></span><span></span><i></i><em>Follow Us</em></div>
</section>

<section class="about">
  <div class="photo-wrap"><div class="photo" role="img" aria-label="Photograph of three colleagues reviewing a tablet together in an office"></div></div>
  <div class="text">
    <h2 class="section">About Us</h2>
    <p class="lorem">Lorem ipsum dolor sit amet, consectetur adipiscing elit, sed do eiusmod tempor incididunt ut labore et dolore magna aliqua. Quis ipsum suspendisse ultrices gravida. Risus commodo viverra maecenas accumsan lacus vel facilisis. Sed in pellentesque nibh commodo nisi duis ut aliquip ex ea commodo consequat. Duis aute irure dolor in reprehenderit in voluptate velit esse cillum dolore eu fugiat nulla pariatur. Excepteur sint occaecat cupidatat non proident, sunt in culpa qui officia deserunt mollit anim.</p>
    <div class="btn"><span class="label">Learn More</span><span class="arrow">→</span></div>
  </div>
</section>

<section class="split">
  <div class="half invest" role="img" aria-label="Blue tinted photo of a handshake over a desk">
    <h3>Invest With Us</h3>
    <p>Lorem ipsum dolor sit amet, consectetur adipiscing elit, sed do eiusmod tempor incididunt ut labore et dolore magna aliqua ut enim ad minim veniam, quis nostrud exercitation ullamco laboris nisi ut aliquip ex ea commodo consequat duis aute irure dolor in reprehenderit in voluptate velit esse cillum dolore eu fugiat nulla pariatur.</p>
    <div class="btn ghost"><span class="label">Learn More</span><span class="arrow">→</span></div>
  </div>
  <div class="half borrow" role="img" aria-label="Blue tinted photo of a couple signing a loan agreement">
    <h3>Borrow With Us</h3>
    <p>Lorem ipsum dolor sit amet, consectetur adipiscing elit, sed do eiusmod tempor incididunt ut labore et dolore magna aliqua ut enim ad minim veniam, quis nostrud exercitation ullamco laboris nisi ut aliquip ex ea commodo consequat duis aute irure dolor in reprehenderit in voluptate velit esse cillum dolore eu fugiat nulla pariatur.</p>
    <div class="btn ghost"><span class="label">Learn More</span><span class="arrow">→</span></div>
  </div>
</section>

<section class="featured">
  <h2 class="section">Featured Investments</h2>
  <div class="cards">
    <article class="card">
      <div class="img" role="img" aria-label="Photo of a large suburban family home" style="background:linear-gradient(180deg,#9fc1e2,#8a7a62 60%,#4d6a3a)"></div>
      <div class="body"><h4>Bills Piling Up?</h4><p class="lorem">Lorem ipsum dolor sit amet consectetur adipiscing elit sed do eiusmod tempor incididunt ut labore et dolore magna aliqua enim minim veniam.</p><div class="more">Read More <span class="circle" style="width:14px;height:14px"></span></div></div>
    </article>
    <article class="card">
      <div class="img" role="img" aria-label="Photo of a family relaxing together at home" style="background:linear-gradient(135deg,#e4d2b8,#a57b55 55%,#5e4636)"></div>
      <div class="body"><h4>Finance Your Project</h4><p class="lorem">Lorem ipsum dolor sit amet consectetur adipiscing elit sed do eiusmod tempor incididunt ut labore et dolore magna aliqua enim minim veniam.</p><div class="more">Read More <span class="circle" style="width:14px;height:14px"></span></div></div>
    </article>
    <article class="card">
      <div class="img" role="img" aria-label="Photo of a modern white house with a green lawn" style="background:linear-gradient(180deg,#b8d4ee,#e6e6e3 55%,#6c8d4c)"></div>
      <div class="body"><h4>Recommended Professionals</h4><p class="lorem">Lorem ipsum dolor sit amet consectetur adipiscing elit sed do eiusmod tempor incididunt ut labore et dolore magna aliqua enim minim veniam.</p><div class="more">Read More <span class="circle" style="width:14px;height:14px"></span></div></div>
    </article>
  </div>
</section>

<section class="testimonials">
  <h2 class="section">Our Testimonials</h2>
  <div class="quotes">
    <article class="quote">
      <span class="mark">”</span>
      <div class="who"><div class="avatar" role="img" aria-label="Portrait of client Dara Quill"></div><div><h4>Dara Quill</h4><div class="stars">
        <svg width="70" height="12" viewBox="0 0 70 12"><g fill="#e23b3b"><path id="s" d="M6 0l1.8 3.9 4.2.4-3.2 2.8 1 4.1L6 9.1 2.2 11.2l1-4.1L0 4.3l4.2-.4z"/><use href="#s" x="14"/><use href="#s" x="28"/><use href="#s" x="42"/><use href="#s" x="56"/></g></svg></div></div></div>
      <p class="lorem">Lorem ipsum dolor sit amet, consectetur adipiscing elit, sed do eiusmod tempor incididunt ut labore et dolore magna aliqua. Ut enim ad minim veniam, quis nostrud exercitation ullamco laboris nisi ut aliquip ex ea commodo.</p>
    </article>
    <article class="quote">
      <span class="mark">”</span>
      <div class="who"><div class="avatar" role="img" aria-label="Portrait of client Teo Marsh"></div><div><h4>Teo Marsh</h4><div class="stars">
        <svg width="70" height="12" viewBox="0 0 70 12"><g fill="#e23b3b"><path id="s2" d="M6 0l1.8 3.9 4.2.4-3.2 2.8 1 4.1L6 9.1 2.2 11.2l1-4.1L0 4.3l4.2-.4z"/><use href="#s2" x="14"/><use href="#s2" x="28"/><use href="#s2" x="42"/><use href="#s2" x="56"/></g></svg></div></div></div>
      <p class="lorem">Lorem ipsum dolor sit amet, consectetur adipiscing elit, sed do eiusmod tempor incididunt ut labore et dolore magna aliqua. Ut enim ad minim veniam, quis nostrud exercitation ullamco laboris nisi ut aliquip ex ea commodo.</p>
    </article>
  </div>
</section>

<section class="contact-form">
  <h2 class="section">Get In Touch</h2>
  <div class="form">
    <div class="field">Your Name</div>
    <div class="field">Email</div>
    <div class="field">Phone Number</div>
    <div class="field">Address</div>
    <div class="field wide">Message:</div>
    <div class="btn submit"><span class="label" style="padding:0 40px">Submit</span><span class="arrow">→</span></div>
  </div>
</section>

<footer class="footer">
  <div class="cols">
    <div class="col">
      <div class="brand"><span class="mark" style="width:30px;height:30px;background:var(--blue)"></span><span>HALVANE<br><span style="font-size:12px;font-weight:600">Capital Group</span></span></div>
      <p style="margin-top:18px">Lorem ipsum dolor sit consectetur adipiscing elit, sed eiusmod tempor</p>
      <div class="follow">FOLLOW US</div>
      <div class="follow-row"><span></span><span></span><span></span><span></span></div>
    </div>
    <div class="col"><h4>Quicklinks</h4><ul><li>Home</li><li>About Us</li><li>Investors</li><li>Borrowers</li><li>Contact Us</li></ul></div>
    <div class="col"><h4>Otherlinks</h4><ul><li>FAQ</li><li>Service</li><li>Team</li><li>Privacy</li><li>Policy</li></ul></div>
    <div class="col"><h4>Contact Us</h4><ul class="contact-list">
      <li><span class="circle"></span>555-0142-770</li>
      <li><span class="circle"></span>info@halvanecapital.example</li>
      <li><span class="circle" style="flex:none"></span>1212, lorem ipsum dolor sit amet adipiscing elit, sed eiusmod</li>
    </ul></div>
  </div>
  <div class="copy">Copyright © 2021 Halvane Capital Group All Rights Reserved.</div>
</footer>

</body>
</html>
```